Web Page for Elearning project

SUMMARY OF REQUIREMENT
The requirement is to provide the graphic design for an eLearning project. I need the design elements for a main page layout which I can recreate in an eLearning authoring program (Lectora) using the graphic design you provide.

SUMMARY OF SITE PAGES
The web site has 11 sections with pages within each section. The user will navigate through all pages by clicking NEXT or by jumping to a page using either an index or table of contents (according to your design).

The sections are:
- Introduction
- TWP Cemeteries
- Ashvale*
- Meadow of Pines (Catholic)*
- Tallow Bend (Catholic)*
- Dunmarrow (Catholic)*
- Wyatts Hollow (Catholic)*
- Meadow of Pines (Presbyterian)*
- Brenta Vale*
- Summary
- Quiz

The sections with a "*" contain consistent pages - which I imagine could be accessed by clicking on a tab or button. I would need you to supply the graphics to be able to set them up in my elearning program. The pages are:
- History
- Map
- Contact
- Directions
- Services
- Sections

ONCE THE DESIGN IS ACCEPTED...
Ultimately I need the background graphics so I can implement the design in my elearning authoring program What else do you need to know?

SEE ATTACHED PDF FOR MORE DETAILS AND EXAMPLES OF WHAT I AM CURRENTLY WORKING WITH

Reason: Project was set up incorrectly for the first 6 days of the job

Reason: Australia now has public holidays for the next 5 days.  Everyone back at work on 27-28 April.

Target Market(s)

The users are mostly middle-aged women who only have basic computer skills... needs to be easy to navigate.

Industry/Entity Type

Graphic Design

Requirements
Must have
• Light, fun but professional. Its training...should have a light/easy feel about it.

Must be easy to look at. The design should support the overall navigation/structure.
Nice to have
• easy to look at, light.
Should not have
• Should not use serif fonts.
I don't think we'd go for bold lime green or any really zany colours.

```html
<!DOCTYPE html>
<html lang="en">
<head>
<meta charset="utf-8">
<title>TWP Cemeteries Module</title>
<link href="https://fonts.googleapis.com/css2?family=Cabin:ital,wght@0,400;0,700;1,700&family=Cabin+Condensed:wght@500&family=Raleway:wght@400&family=Arimo:wght@700&display=swap" rel="stylesheet">
<style>
  :root {
    --maroon: #8c1a30;
    --maroon-dark: #6e0f22;
    --maroon-light: #b32a45;
    --title-blue: #0b4e9c;
    --nav-top: #0c5cc0;
    --nav-bottom: #0a2f6e;
    --nav-rule: rgba(255,255,255,0.22);
    --btn-top: #bfe8ff;
    --btn-bottom: #3aaaf0;
    --btn-ink: #0b2a5c;
    --bubble-top: #eef2fb;
    --bubble-bottom: #a9b9e2;
    --bubble-edge: #1e5fc4;
    --cloud: #1f5f96;
    --ink: #1b2340;
    --floor: #e6e6e8;
    --page-grey: #d9dde2;
    --white: #ffffff;
  }
  * { box-sizing: border-box; margin: 0; padding: 0; }
  html, body { width: 1200px; height: 900px; overflow: hidden; background: var(--white); }
  .canvas {
    position: relative; width: 1200px; height: 900px; overflow: hidden;
    background: linear-gradient(to bottom, var(--white) 0, var(--white) 520px, var(--floor) 860px, #f2f2f3 900px);
    font-family: "Cabin", sans-serif;
  }
  .frame {
    position: absolute; left: 18px; top: 17px; width: 1164px; height: 827px;
    border: 2px solid var(--maroon);
    background: linear-gradient(to bottom, var(--white) 0, var(--white) 500px, #eeeeef 660px, #f3f3f4 827px);
  }
  .module-tab {
    position: absolute; left: 18px; top: 17px; width: 256px; height: 53px;
    background: linear-gradient(to bottom, var(--maroon-light), var(--maroon) 55%, var(--maroon-dark));
    clip-path: polygon(0 0, 222px 0, 256px 53px, 0 53px);
    color: var(--white); font-family: "Cabin Condensed", sans-serif; font-weight: 500;
    font-size: 22px; line-height: 42px; padding-left: 10px; white-space: nowrap;
  }
  .course-title {
    position: absolute; left: 298px; top: 26px; white-space: nowrap;
    font-family: "Arimo", sans-serif; font-weight: 700; font-size: 36px; color: var(--title-blue);
  }
  .title-rule { position: absolute; left: 300px; top: 72px; width: 586px; border-top: 1px dashed var(--title-blue); }
  .nav-buttons { position: absolute; top: 34px; left: 910px; display: flex; gap: 6px; }
  .nav-btn {
    height: 32px; border-radius: 16px; border: 1px solid #2a86c9;
    background: linear-gradient(to bottom, var(--btn-top), #7ccaf6 50%, var(--btn-bottom));
    color: var(--btn-ink); font-weight: 700; font-style: italic; font-size: 17px;
    display: flex; align-items: center; justify-content: center; gap: 6px;
    box-shadow: 0 1px 2px rgba(0,0,0,0.25); white-space: nowrap;
  }
  .nav-btn.back, .nav-btn.next { width: 84px; }
  .nav-btn.close { width: 84px; margin-left: 2px; }
  .nav-btn svg { width: 14px; height: 14px; }
  .section-index {
    position: absolute; left: 22px; top: 72px; width: 218px; height: 290px;
    background: linear-gradient(to bottom, var(--nav-top), var(--nav-bottom));
    border: 1px solid #062050; list-style: none; padding: 4px 4px;
  }
  .section-index li {
    height: 31px; line-height: 31px; padding-left: 8px;
    color: var(--white); font-weight: 700; font-style: italic; font-size: 15.5px;
    letter-spacing: -0.2px; white-space: nowrap;
    border-bottom: 1px solid var(--nav-rule);
  }
  .section-index li:last-child { border-bottom: none; }
  .guide-figure {
    position: absolute; left: 252px; top: 156px; width: 300px; height: 456px;
    border-radius: 40px 40px 60px 60px;
    background: linear-gradient(to bottom, #f4f5f7, #d9dce2 70%, #33508a 100%);
  }
  .hint-cloud { position: absolute; left: 252px; top: 84px; width: 134px; height: 116px; }
  .hint-cloud p {
    position: absolute; left: 0; top: 30px; width: 134px; text-align: center;
    color: var(--white); font-family: "Raleway", sans-serif; font-size: 14.5px; line-height: 19px;
  }
  .speech { position: absolute; left: 528px; top: 182px; width: 580px; height: 302px; }
  .speech-box {
    position: absolute; left: 124px; top: 2px; width: 450px; height: 296px;
    border-radius: 34px; border-top: 8px solid var(--bubble-edge);
    background: linear-gradient(to bottom, var(--bubble-top), #cdd7f0 55%, var(--bubble-bottom));
    box-shadow: 3px 5px 6px rgba(0,0,0,0.35);
    padding: 30px 18px 0 20px;
    font-family: "Raleway", sans-serif; font-size: 15px; line-height: 20.5px; color: var(--ink);
  }
  .speech-box p + p { margin-top: 20px; }
  .brand {
    position: absolute; left: 26px; top: 770px; display: flex; align-items: center; gap: 6px;
    color: var(--title-blue); font-size: 14px; font-weight: 700; white-space: nowrap;
  }
  .brand i { width: 12px; height: 12px; border-radius: 50%; background: var(--maroon); display: block; }
  .page-counter {
    position: absolute; left: 1084px; top: 802px; width: 92px; height: 36px;
    background: var(--page-grey); color: var(--ink); font-size: 15px;
    display: flex; align-items: center; padding-left: 8px; white-space: nowrap;
  }
  .page-counter i {
    position: absolute; right: 4px; top: 6px; width: 24px; height: 24px; border-radius: 50%;
    background: radial-gradient(circle at 40% 35%, #ffffff, #b9c2cc);
  }
</style>
</head>
<body>
<div class="canvas">
  <div class="frame"></div>

  <div class="module-tab">TWP Cemeteries Module</div>
  <h1 class="course-title">Course Subtitle</h1>
  <div class="title-rule"></div>

  <div class="nav-buttons">
    <div class="nav-btn back">Back
      <svg viewBox="0 0 14 14"><path d="M4 2 L10 7 L4 12" fill="none" stroke="#ffffff" stroke-width="2.4"/></svg>
    </div>
    <div class="nav-btn next">
      <svg viewBox="0 0 14 14"><path d="M10 2 L4 7 L10 12" fill="none" stroke="#ffffff" stroke-width="2.4"/></svg>Next
    </div>
    <div class="nav-btn close">Close
      <svg viewBox="0 0 14 14"><circle cx="7" cy="7" r="7" fill="#e8f4ff"/><path d="M4.5 4.5 L9.5 9.5 M9.5 4.5 L4.5 9.5" stroke="#3a7fc0" stroke-width="1.8"/></svg>
    </div>
  </div>

  <ul class="section-index">
    <li>Introductions</li>
    <li>TWP Cemeteries</li>
    <li>Ashvale</li>
    <li>Meadow of Pines( Catholic)</li>
    <li>Tallow Bend (Catholic)</li>
    <li>Wyatts Hollow (Catholic)</li>
    <li>Brenta Vale</li>
    <li>Summary</li>
    <li>Quick Quiz</li>
  </ul>

  <div class="guide-figure" role="img" aria-label="Cartoon guide character pointing up towards the section index"></div>

  <div class="hint-cloud">
    <svg width="134" height="116" viewBox="0 0 134 116">
      <path d="M30 22 C34 4 58 0 68 12 C78 0 104 4 106 22 C124 24 134 44 124 60 C134 76 120 98 100 94 C92 110 70 112 62 100 C50 112 26 108 24 92 C6 92 0 72 10 60 C0 46 10 24 30 22 Z" fill="var(--cloud)" stroke="#0d3c66" stroke-width="1.5"/>
    </svg>
    <p>Click Here,<br>I`ll show you<br>the index</p>
  </div>

  <div class="speech">
    <svg width="140" height="160" viewBox="0 0 140 160" style="position:absolute;left:0;top:0">
      <polygon points="0,40 128,30 128,150" fill="#dfe6f6" stroke="#9eb2de" stroke-width="1"/>
    </svg>
    <div class="speech-box">
      <p>The first time you read this module you might want to read all the way through. Just keep clickinh the NEXT button to read every page.</p>
      <p>If you want to find information about a cemetry, jump to the cemetery page using the index on the left. Read this module as many times as yu want if you have questions ask your supervisor.</p>
      <p>At the end of the module you can complete a short quiz. It’s fun so h e a go to see&nbsp; how much you have learnt!</p>
    </div>
  </div>

  <div class="brand"><i></i>TWP Cemeteries</div>

  <div class="page-counter">Page :<i></i></div>
</div>
</body>
</html>
```